Deliver a professional and engaging investment propsal.

I am appealing to highend smart investors and need a high quality, engaging and formal presentation in PDF.
DropBox: https://www.filemarsh.net/sh/q8wz3kdmv2tanp7/BCxRp4LfWmZq9TnYeJ2sKo7vH?dl=0
Text for project is in Dropbox called New Proposal Final
Along with past much older attempts of this job.
Any additional ideas to enable a better outcome would be appreicated.

```html
<!DOCTYPE html>
<html lang="en">
<head>
<meta charset="utf-8">
<title>Arrow X Business Park – Project Proposal</title>
<link rel="stylesheet" href="https://fonts.googleapis.com/css2?family=Montserrat:wght@500;700;800&family=Open+Sans:wght@400;600;700&display=swap">
<style>
:root{
  --blue:#2f6fd0;
  --blue-dark:#1d4e9e;
  --ink:#333a44;
  --paper:#ffffff;
  --ground:#e6e7e9;
  --green:#9ccf72;
  --green-light:#d9efc6;
  --row-blue:#6fa3e0;
  --line:#c9ced6;
}
*{box-sizing:border-box;margin:0;padding:0}
html,body{width:1200px;height:2416px;overflow:hidden;background:var(--ground)}
body{position:relative;font-family:"Open Sans",Arial,sans-serif;color:var(--ink)}

/* ---------- cover ---------- */
.cover{position:absolute;left:330px;top:60px;width:540px;height:760px;background:var(--paper);box-shadow:0 8px 24px rgba(0,0,0,.18);overflow:hidden}
.cover-photo{position:absolute;left:14px;top:0;right:0;bottom:44px;background:linear-gradient(180deg,#2a63c9 0%,#4f8be0 38%,#8a7768 62%,#6d6058 78%,#b9b6b0 100%)}
.cover-bar-bottom{position:absolute;left:0;right:0;bottom:0;height:22px;background:var(--blue)}
.cover-bar-left{position:absolute;left:0;bottom:0;width:14px;height:200px;background:var(--blue)}
.cover-corner{position:absolute;right:0;top:40px;width:20px;height:140px;background:var(--blue)}
.cover-title{position:absolute;left:14px;right:0;top:62px;text-align:center;color:#fff;font-family:"Montserrat",Arial,sans-serif}
.cover-kicker{font-size:24px;font-weight:500;letter-spacing:.5px}
.cover-name{font-size:66px;font-weight:800;line-height:1;margin-top:4px}
.cover-sub{display:inline-block;font-size:38px;font-weight:500;border-top:3px solid #fff;border-bottom:3px solid #fff;padding:2px 10px;margin-top:6px;line-height:1.15}
.cover-ribbon{position:absolute;right:0;top:560px;width:430px;height:56px;background:#fff;display:flex;align-items:center;justify-content:center;font-family:"Montserrat",Arial,sans-serif;font-weight:700;font-size:23px;color:var(--blue-dark)}

/* ---------- pages ---------- */
.page{position:absolute;width:445px;height:620px;background:var(--paper);box-shadow:0 3px 12px rgba(0,0,0,.16);overflow:hidden;font-size:6.6px;line-height:1.42}
.p1{left:132px;top:1114px}.p2{left:620px;top:1114px}
.p3{left:132px;top:1768px}.p4{left:620px;top:1768px}
.page::before{content:"";position:absolute;right:0;bottom:0;width:120px;height:8px;background:var(--blue)}
.page::after{content:"";position:absolute;right:0;bottom:0;width:8px;height:90px;background:var(--blue)}
.edge-left{position:absolute;left:0;bottom:0;width:8px;height:70px;background:var(--blue)}

.tab{position:absolute;left:0;height:22px;display:flex;align-items:center;padding:0 22px 0 24px;background:var(--blue);color:#fff;font-family:"Montserrat",Arial,sans-serif;font-weight:700;font-size:10.5px;letter-spacing:.3px}
.tab::after{content:"";position:absolute;right:-14px;top:0;border-left:14px solid var(--blue-dark);border-top:22px solid transparent}
.body{position:absolute;left:24px;right:24px}
.body p{margin-bottom:5px}

.photo{position:absolute}
.bullets{list-style:none}
.bullets li{position:relative;padding-left:14px;margin-bottom:7px}
.bullets li::before{content:"";position:absolute;left:0;top:1px;width:0;height:0;border-left:7px solid var(--blue);border-top:4px solid transparent;border-bottom:4px solid transparent}
.cols{display:grid;grid-template-columns:1fr 1fr;column-gap:16px}

.growth{display:grid;grid-template-columns:repeat(3,1fr);gap:8px}
.growth div{border:1.5px solid var(--blue);border-radius:5px;padding:8px 4px;text-align:center;font-family:"Montserrat",Arial,sans-serif;font-weight:700;font-size:7.4px;line-height:1.25;color:var(--blue-dark)}

.sens{width:100%;border-collapse:collapse;font-size:6.4px}
.sens td,.sens th{border:1px solid #fff;padding:2.2px 4px;text-align:center;background:#eef1f5}
.sens td:first-child,.sens th:first-child{text-align:right;font-weight:700;width:40%}
.sens th{background:var(--green);font-weight:700}
.sens .hl td{background:var(--green-light);font-weight:700}
.sens .bl td{background:var(--row-blue);font-weight:700}
.sens .gr td{background:var(--green);font-weight:700}
.sens .sub td{background:#fff;text-align:left;font-weight:700}
.closing{font-size:9px;line-height:1.35}
</style>
</head>
<body>

<section class="cover">
  <div class="cover-photo" role="img" aria-label="Dusk photograph of a multi-storey hotel with a stone and red-framed entrance canopy under a blue sky"></div>
  <div class="cover-bar-left"></div>
  <div class="cover-bar-bottom"></div>
  <div class="cover-corner"></div>
  <div class="cover-title">
    <div class="cover-kicker">Project Proposal</div>
    <div class="cover-name">ARROW X</div>
    <div class="cover-sub">BUSINESS PARK</div>
  </div>
  <div class="cover-ribbon">60 Acre mixed-use development</div>
</section>

<!-- Page: Proposal -->
<section class="page p1">
  <div class="edge-left"></div>
  <div class="tab" style="top:22px">PROPOSAL</div>
  <div class="body" style="top:58px">
    <p>We have an incredible property, Arrow X Business Park, located at 1180 Prairie Route 12, Kestrel County, Harlow City, North Dakota 58800 USA which we have fully funded with cash and now need a joint venture partner, buyer or lender to get this project to completion and producing a substantial profit we all can share.</p>
  </div>
  <div class="photo" role="img" aria-label="Colour site plan of the business park with lots, roads and small photos of planned buildings" style="left:24px;top:104px;width:170px;height:128px;background:linear-gradient(160deg,#dfe8d8,#b9cfae 55%,#8fa6b8)"></div>
  <div class="body" style="top:112px;left:208px">
    <p>Our property is located on the best oil reserves in the world in North Dakota USA, with more oil than any other county in the Bakken Basin and with the lowest recoverable costs of $24 a barrel.</p>
    <p>We own the property and need a partner to develop the site and bring to the market at half the cost of competing business parks in the area.</p>
  </div>
  <div class="tab" style="top:250px">PARTICIPATION OPTIONS</div>
  <div class="body cols" style="top:290px">
    <ul class="bullets">
      <li>A joint venture partner would support all the costs developing the property without the upfront costs of the property purchase.</li>
      <li>Contract drawn up protecting and supporting both parties on agreed terms.</li>
      <li>Joint venture partner to supply the development costs estimated to be around $65,000 an acre estimated pending tender selection and additional refundable security bonds held with Harlow City on development works.</li>
      <li>A buyer can be fully supported by myself to oversee the full project and outcomes and support the budgets of construction and sales to get the highest returns for a small fee.</li>
      <li>Financing an excellent terms allowing 12 to 18 months for income streams and could be linked to a joint venture option / profit share.</li>
    </ul>
    <ul class="bullets">
      <li>All sales would be split to ensure both parties are paid out in such a way that both are paid out in full at the same time then a 50/50 profit share split on all remaining sales.</li>
      <li>As a potential joint venture partner, I would cover the full property (57 acres) cost as mentioned of $126,784 per acre (57 acres) $7,200,000.</li>
      <li>Development costs could be in up to three stages to lower outlay and limit exposure if so desired, however it will take longer to complete and bring to market.</li>
      <li>To purchase the property, you would need to contact me directly and I can introduce you to our realtor who will discount his commission from 6% to 5% which is a significant saving.</li>
    </ul>
  </div>
</section>

<!-- Page: Major site changes -->
<section class="page p2">
  <div class="edge-left"></div>
  <div class="tab" style="top:22px">MAJOR SITE CHANGES</div>
  <div class="photo" role="img" aria-label="Aerial photograph of the cleared development site beside the highway with annotation callouts" style="left:24px;top:52px;right:24px;height:160px;background:linear-gradient(170deg,#a9a79e,#8f8a7c 45%,#b8a793 70%,#9a9486)"></div>
  <div class="body cols" style="top:226px">
    <ul class="bullets">
      <li>We purchased the property in 2013 for cash and without any additional debt, at the time we had highway 85 frontage just outside Harlow City limits South of town with a zoning of agricultural within Kestrel County.</li>
      <li>Hotel site purchased 2014 now with the option to purchase the franchise license and build the hotel ourselves.</li>
      <li>In 2016 the new bypass opened intersecting our highway frontage just 100 yards away which brings all the traffic in the Bakken right past our site which was a massive win for this project.</li>
      <li>Some commercial property listed across the road at $750,000 per acre retail at Fieldstone Commons and other business parks average listings $550,000 per acre.</li>
      <li>May 2018 Full site infrastructure development approval which includes all roads and city services, this will trigger interest in the site from passing traffic and with a great marketing campaign will surely start sales coming in quickly once we break ground and start work.</li>
    </ul>
    <ul class="bullets">
      <li>2014 site zoning changed allowing a commercial zoning.</li>
      <li>In 2016 we were added into City Limits which was a massive improvement to our site now taking advantage of confirmed city water and sewer was a great outcome.</li>
      <li>In 2016 we were added into City Limits which was a massive improvement to our site now taking advantage of confirmed city water and sewer was a great outcome.</li>
      <li>In late 2017 we applied for full site development application and were approved in mid-2018 which again was a significant improvement to the project.</li>
      <li>We can also buy the franchise license of the Prairie Crest hotel for additional income potential if desired.</li>
    </ul>
  </div>
  <div class="photo" role="img" aria-label="Photograph of two people shaking hands in soft daylight" style="left:150px;top:500px;right:24px;height:92px;background:linear-gradient(90deg,rgba(255,255,255,0),#e8d9c4 40%,#c8b49c 70%,#f1ebe2)"></div>
</section>

<!-- Page: Location -->
<section class="page p3">
  <div class="edge-left"></div>
  <div class="tab" style="top:22px">LOCATION</div>
  <div class="body" style="top:60px">
    <p>Our property is ideally located in Harlow City, United States of America, despite its humble beginnings, has suddenly found itself at the epicentre of the Bakken oil boom. Located in Western North Dakota the city has seen workers flood into the area over recent years to fill positions to support the growth.</p>
    <p>Kestrel County where Harlow City is located has more recoverable oil and gas at the lowest recoverable cost per barrel at $24, making it most affordable anywhere in the Bakken basin, centrally located and very desirable area to establish a business and company headquarters.</p>
    <p>Harlow City is the crossroads whereby around 20,000 vehicles pass by our site each day travelling locally and between Williston where boom started and Dickinson an established town with relevant established support for business and infrastructure. Our project has highway frontage and is 100 yards away from the bypass intersection making it the best location in Kestrel County for this type of project.</p>
    <p>With billions invested into infrastructure in the past 5 years in and around Bakken Shale Oil Basin our project has become the beneficiary of a major new Harlow City bypass which intersects highway 85 just 100 yards south of our project, putting us on one of the busiest intersections in the Bakken. With this rapid growth we were included into the Harlow City limits providing additional benefits to the overall success for our development including all city services.</p>
    <p>Demand stems from the ongoing boom in oil and gas drilling in the area which is still in its infancy stages of this North Dakota oil play, and is expected to continue to grow well past 2050 based on all available reserves beneath the ground.</p>
  </div>
  <div class="tab" style="top:326px">ADDITIONAL LOCATION GROWTH</div>
  <div class="body growth" style="top:366px">
    <div>NORTHGATE 150<br>MILLION-DOLLAR<br>HARLOW CITY<br>INVESTMENT 2018</div>
    <div>NORTH DAKOTA IS THE<br>NATION'S<br>SECOND-BIGGEST OIL<br>PRODUCER</div>
    <div>KESTREL COUNTY<br>INVESTMENT<br>DEVELOPMENT</div>
  </div>
  <div class="body" style="top:430px">
    <p>Within the 100 yards of Arrow X Business park, directly across the road commercial land is currently listed at of $750,000 an acre at Fieldstone Commons and many more locations up to $650,000 per acre. With an advantage over other sites in terms of a better location and much lower purchase and development costs the numbers don't lie, and we need to have and ready to build lots to offer the market.</p>
    <p>Bakken traffic, North, South, East and West will have to travel right by our site making it the second busiest intersection in the Bakken area, giving us the best exposure to sell, promote and grow, this site can and will be the location for new business and growth, we need to develop the site now to move forward.</p>
    <p>With our obvious high exposure to potential buyers through the passing traffic and lower entry price point there is no doubt Arrow X Town Center will become the place where business will want to build alongside a quality business like the Prairie Crest Extended Stay Hotel.</p>
  </div>
</section>

<!-- Page: Extended stay & sensitivity -->
<section class="page p4">
  <div class="edge-left"></div>
  <div class="tab" style="top:22px">THE PRAIRIE CREST EXTENDED STAY</div>
  <div class="body" style="top:60px">
    <p>Prairie Crest Inn's unmatched experience and leadership in the hotel industry designed a new extended stay hotel that satisfy one of the most in-demand needs of today's business and leisure travellers.<br>Here guests will experience the very best in hotel and home. Its flexible spaces, stylish design, and brand signature elements come together to create an enriching extended stay experience for your guests, while building loyalty and repeat bookings for your hotel.</p>
  </div>
  <div class="tab" style="top:122px">SENSITIVITY ANALYSIS</div>
  <div class="body" style="top:158px">
    <p>Sensitivity analysis is based on sales of the full site (45 saleable acres) Our numbers below don't include revenue from build to suit projects or potential income stream from construction of the hotel and various projects that could be developed on this 60 acre site. These costs are only shown as estimates at this stage.</p>
  </div>
  <div class="body" style="top:196px">
    <table class="sens">
      <tr><th>Estimated Projections</th><th>Projected</th><th>Best Scenario</th><th>Worst Scenario</th></tr>
      <tr class="hl"><td>Average sale per acre (45)</td><td>$450,000</td><td>$500,000</td><td>$350,000</td></tr>
      <tr class="hl"><td>Total Sales</td><td>$20,250,000</td><td>$22,500,000</td><td>$15,750,000</td></tr>
      <tr class="sub"><td colspan="4">Projected Expenses</td></tr>
      <tr><td>Engineers</td><td>$250,000</td><td>$190,000</td><td>$300,000</td></tr>
      <tr><td>Estimated Site Development Works</td><td>$2,400,000</td><td>$2,000,000</td><td>$3,500,000</td></tr>
      <tr><td>Site Licences / Permits</td><td>$450,000</td><td>$350,000</td><td>$500,000</td></tr>
      <tr><td>Additional Signage, Marketing</td><td>$20,000</td><td>$15,000</td><td>$25,000</td></tr>
      <tr><td>Professional Fees</td><td>$135,000</td><td>$130,000</td><td>$145,000</td></tr>
      <tr><td>Attorney Contracts / Support</td><td>$45,000</td><td>$30,000</td><td>$50,000</td></tr>
      <tr><td>Realtor Commissions</td><td>$1,000,000</td><td>$900,000</td><td>$1,200,000</td></tr>
      <tr><td>Property Payout</td><td>$7,200,000</td><td>$7,200,000</td><td>$7,200,000</td></tr>
      <tr class="bl"><td>Estimated Projected Full Costs</td><td>$11,500,000</td><td>$10,815,000</td><td>$12,920,000</td></tr>
      <tr class="bl"><td>Estimated Projected Per Acre Costs</td><td>$255,000</td><td>$240,000</td><td>$287,000</td></tr>
      <tr class="gr"><td>Estimated Total Projected Profit</td><td>$8,750,000</td><td>$11,685,000</td><td>$2,830,000</td></tr>
      <tr class="gr"><td>Estimated Profit Each Partner</td><td>$4,375,000</td><td>$5,842,500</td><td>$1,415,000</td></tr>
    </table>
  </div>
  <div class="body closing" style="top:540px">This investment may offer an opportunity for a visa into the USA however you will need to undertake your own inquires.</div>
</section>

</body>
</html>
```